Corvelle BSH Book Cover Design: Book 1 of 4

Designers must not submit more than 1 design. Submission of multiple designs will result in disqualification.

Designer must be highly experienced with properly designing and formatting Corvelle BSH book covers. The winner of this contest will receive three more covers to do. This project is for one of four books in a series. I want the same designer to do all four books because they are in a series and need to look the same. Attached are the directions and files.

Target Market(s)

see attachments

Industry/Entity Type

see attachments

Requirements
Must have
• see attachments
Nice to have
• see attachments
Should not have
• see attachments

```html
<!DOCTYPE html>
<html lang="en">
<head>
<meta charset="UTF-8">
<title>Before You Pay – Full Cover</title>
<link href="https://fonts.googleapis.com/css2?family=Bebas+Neue&family=Anton&family=Montserrat:wght@400;500;600;700&family=Oswald:wght@400;500;600&display=swap" rel="stylesheet">
<style>
  :root{
    --navy:#0c2349;
    --navy-deep:#081a3a;
    --orange:#f7860f;
    --white:#ffffff;
    --paper:#e9ecf1;
  }
  *{margin:0;padding:0;box-sizing:border-box}
  html,body{width:1200px;height:762px;overflow:hidden;background:var(--navy)}
  .cover{position:relative;width:1200px;height:762px;background:var(--navy);color:var(--white);font-family:'Montserrat',sans-serif;overflow:hidden}
  .rule{position:absolute;height:3px;background:var(--orange)}

  /* back cover */
  .back-title{position:absolute;left:0;width:590px;top:52px;text-align:center;font-family:'Bebas Neue',sans-serif;font-size:80px;letter-spacing:1px;color:var(--paper);line-height:1}
  .accent{color:var(--orange)}
  .back-copy{position:absolute;left:62px;top:191px;width:470px;font-size:9.4px;line-height:1.2;color:var(--white)}
  .back-copy h3{color:var(--orange);font-weight:500;font-size:9.6px;margin-bottom:3px}
  .back-copy p{margin-bottom:8px;text-align:justify}
  .back-copy ul{list-style:none;margin:0 0 6px 18px}
  .back-copy li{margin-bottom:5.4px;padding-left:14px;position:relative}
  .back-copy li::before{content:"•";position:absolute;left:0}
  .back-copy .section{margin-top:4px}
  .back-tagline{position:absolute;left:0;width:590px;top:679px;text-align:center;font-weight:600;font-size:17.5px;line-height:1.25;letter-spacing:.3px}
  .back-tagline em,.front-kicker em{color:var(--orange);font-style:italic;font-weight:500}

  /* spine */
  .spine-title{position:absolute;left:614px;top:58px;writing-mode:vertical-rl;font-family:'Bebas Neue',sans-serif;font-size:25px;letter-spacing:.5px;color:var(--paper);line-height:1}
  .spine-wheel{position:absolute;left:589px;top:515px}
  .spine-author{position:absolute;left:598px;top:548px;writing-mode:vertical-rl;font-family:'Oswald',sans-serif;font-weight:600;font-size:13px;letter-spacing:.3px;line-height:1}
  .spine-creds{position:absolute;left:588px;top:554px;writing-mode:vertical-rl;font-family:'Oswald',sans-serif;font-size:4.6px;letter-spacing:.2px;color:var(--paper)}

  /* front cover */
  .front-photo{position:absolute;left:640px;top:282px;width:560px;height:368px;
    background:
      radial-gradient(ellipse 45% 35% at 62% 42%, rgba(240,170,90,.85), rgba(240,170,90,0) 70%),
      linear-gradient(180deg,#1b3558 0%,#4a5f7e 28%,#a98b6d 48%,#3b5475 62%,#1b3252 80%,#0e2547 100%);
    -webkit-mask-image:linear-gradient(90deg,transparent 0%,rgba(0,0,0,.5) 18%,#000 40%);
            mask-image:linear-gradient(90deg,transparent 0%,rgba(0,0,0,.5) 18%,#000 40%)}
  .front-kicker{position:absolute;left:640px;width:560px;top:44px;text-align:center;font-weight:600;font-size:11.2px;line-height:1.3;letter-spacing:.3px}
  .kicker-line{display:inline-block;width:24px;height:1.5px;background:var(--orange);vertical-align:middle;margin:0 5px}
  .front-title{position:absolute;left:712px;top:84px;font-family:'Anton',sans-serif;font-size:88px;letter-spacing:3px;line-height:1;color:var(--white)}
  .front-pay{position:absolute;left:848px;top:180px;font-family:'Anton',sans-serif;font-size:82px;letter-spacing:3px;line-height:1;color:var(--orange)}
  .anchor-mark{position:absolute;left:722px;top:193px}
  .front-blurb{position:absolute;left:697px;top:228px;width:120px;text-align:center;font-weight:700;font-size:7px;line-height:1.23}
  .front-blurb span{color:var(--orange)}
  .seal{position:absolute;left:1013px;top:193px;width:70px;height:70px;border-radius:50%;background:var(--navy-deep);border:1.5px solid var(--orange);text-align:center;font-size:5px;font-weight:500;line-height:1.5;padding-top:11px}
  .seal svg{display:block;margin:0 auto 3px}
  .seal .hl{color:var(--orange)}

  .features{position:absolute;left:687px;top:348px;list-style:none}
  .feature{display:flex;align-items:center;height:44.5px}
  .feature-icon{width:34px;height:34px;border-radius:50%;background:var(--orange);display:flex;align-items:center;justify-content:center;margin-right:29px;flex:none}
  .feature-text{font-weight:600;font-size:9.3px;line-height:1.2;letter-spacing:.3px;text-shadow:0 1px 2px rgba(0,0,0,.5)}

  .front-wheel{position:absolute;left:899px;top:628px}
  .front-author{position:absolute;left:640px;width:560px;top:678px;text-align:center;font-family:'Bebas Neue',sans-serif;font-size:43px;letter-spacing:1.5px;line-height:1}
  .front-creds{position:absolute;left:640px;width:560px;top:724px;text-align:center;font-family:'Oswald',sans-serif;font-size:12px;letter-spacing:.8px;color:var(--orange)}
</style>
</head>
<body>
<main class="cover">

  <!-- back cover -->
  <h2 class="back-title">Before You <span class="accent">Pay</span></h2>
  <div class="rule" style="left:0;top:155px;width:560px"></div>

  <section class="back-copy">
    <h3>Before You Pay:</h3>
    <p>Before you spend thousands on a boat... spend a few hours learning what experienced boaters wish they knew.</p>
    <p>Buying a recreational boat is exciting—but it can also be expensive, confusing, and full of costly mistakes.</p>
    <p>This practical guide helps first-time buyers understand how to evaluate boats, compare ownership options, recognize hidden costs, and avoid expensive surprises before signing the paperwork. Through easy-to-follow explanations, checklists, comparison tables, and illustrations, you'll gain the confidence to make informed decisions and purchase a boat that truly fits your lifestyle.</p>
    <p>Whether you're shopping for your first boat or upgrading to your next one, this book will help you buy smarter and avoid the mistakes that many owners only discover after it's too late.</p>
    <h3 class="section">You'll Learn How To:</h3>
    <ul>
      <li>Choose the right boat</li>
      <li>Compare ownership options</li>
      <li>Inspect boats with confidence</li>
      <li>Understand engines and systems</li>
      <li>Estimate ownership costs</li>
      <li>Avoid common buying mistakes</li>
      <li>Know when to hire a surveyor</li>
      <li>Negotiate from an informed position</li>
    </ul>
    <h3 class="section">About the Author</h3>
    <p>Captain Dalen R. Holtwick is a U.S. Coast Guard Licensed Captain, certified boating instructor, military veteran, and experienced recreational boater. Having trained thousands of students and delivered hundreds of vessels, he created the Before You… series to help new boaters avoid costly mistakes and enjoy safer, more rewarding time on the water.</p>
    <h3 class="section">Series Tagline</h3>
    <p style="margin-bottom:4px">The Before You… Series</p>
    <p>Helping new recreational boaters make smarter decisions before buying, boating, and traveling.</p>
  </section>

  <div class="rule" style="left:0;top:650px;width:560px"></div>
  <p class="back-tagline">THE SMART BUYER'S GUIDE TO FINDING<br>THE RIGHT <em>BOAT</em> AND BOATING WITH CONFIDENCE</p>

  <!-- spine -->
  <div class="spine-title">Before You <span class="accent">Pay</span></div>
  <svg class="spine-wheel" width="24" height="24" viewBox="0 0 24 24" aria-hidden="true">
    <g stroke="var(--orange)" fill="none" stroke-width="1.6">
      <circle cx="12" cy="12" r="7"/><circle cx="12" cy="12" r="2"/>
      <path d="M12 1v22M1 12h22M4.2 4.2l15.6 15.6M19.8 4.2 4.2 19.8"/>
    </g>
  </svg>
  <div class="spine-author">BY CAPTAIN DALEN R. HOLTWICK</div>
  <div class="spine-creds">USCG LICENSED CAPTAIN • CERTIFIED BOATING INSTRUCTOR • VETERAN</div>

  <!-- front cover -->
  <div class="front-photo" role="img" aria-label="Photograph of a white motor boat with a bimini top speeding past a cable-stayed bridge at sunset"></div>

  <p class="front-kicker"><span class="kicker-line"></span>THE SMART BUYER'S GUIDE TO FINDING<span class="kicker-line"></span><br>THE RIGHT <em>BOAT</em> AND BOATING WITH CONFIDENCE</p>
  <h1 class="front-title">BEFORE YOU</h1>
  <div class="front-pay">PAY</div>

  <svg class="anchor-mark" width="76" height="28" viewBox="0 0 76 28" aria-hidden="true">
    <g stroke="var(--orange)" fill="none" stroke-width="2" stroke-linecap="round">
      <path d="M2 16h16M58 16h16"/>
      <circle cx="38" cy="4" r="2.5"/>
      <path d="M38 7v19M32 11h12M28 18c2 6 6 8 10 8s8-2 10-8"/>
    </g>
  </svg>
  <p class="front-blurb">A COMPLETE GUIDE FOR<br><span>FIRST TIME BOAT BUYERS</span><br>FROM SHOPING TO SEA<br>TRIAL AND BEYOND</p>

  <div class="seal">
    <svg width="36" height="14" viewBox="0 0 36 14" aria-hidden="true">
      <g stroke="var(--orange)" fill="none" stroke-width="1.2">
        <path d="M1 7h8M27 7h8"/><circle cx="18" cy="7" r="5.5"/><path d="M15.5 9.5l4-4 1 1-4 4z"/>
      </g>
    </svg>
    AVOID COSTLY<br>MISTAKES<br>BUY WITH<br><span class="hl">CONFIDENCE</span>
  </div>

  <div class="rule" style="left:640px;top:278px;width:560px"></div>

  <ul class="features">
    <li class="feature">
      <span class="feature-icon"><svg width="18" height="18" viewBox="0 0 18 18" aria-hidden="true"><g stroke="#fff" stroke-width="2.2" fill="none" stroke-linecap="round"><circle cx="7" cy="7" r="5"/><path d="M11 11l5 5"/></g></svg></span>
      <span class="feature-text">FIND THE RIGHT BOAT<br>FOR YOUR NEEDS<br>AND BUDGET</span>
    </li>
    <li class="feature">
      <span class="feature-icon"><svg width="18" height="18" viewBox="0 0 18 18" aria-hidden="true"><g stroke="#fff" stroke-width="1.8" fill="none" stroke-linecap="round"><circle cx="9" cy="9" r="7.5"/><path d="M5.5 9l2.5 2.5 5-5.5"/></g></svg></span>
      <span class="feature-text">SHOP SMART<br>AND AVOID<br>RED FLAGS</span>
    </li>
    <li class="feature">
      <span class="feature-icon"><svg width="18" height="18" viewBox="0 0 18 18" aria-hidden="true"><path d="M9 1 L9 13 L2 13 Z M10.5 4 L15 13 L10.5 13 Z M2 15 H16 L14.5 17 H3.5 Z" fill="#fff"/></svg></span>
      <span class="feature-text">SEA TRIAL<br>LIKE A PRO</span>
    </li>
    <li class="feature">
      <span class="feature-icon"><svg width="16" height="18" viewBox="0 0 16 18" aria-hidden="true"><g stroke="#fff" stroke-width="1.5" fill="none"><rect x="1.5" y="2.5" width="13" height="14.5" rx="1.5"/><rect x="5" y="1" width="6" height="3" rx="1"/><path d="M4 8h8M4 11h8M4 14h5"/></g></svg></span>
      <span class="feature-text">INSPECTIONS,<br>SURVEY &amp;<br>NEGOTIATIONS</span>
    </li>
    <li class="feature">
      <span class="feature-icon" style="font-weight:700;font-size:20px;color:#fff">$</span>
      <span class="feature-text">UNDERSTAND TRUE<br>OWNERSHIP COST</span>
    </li>
  </ul>

  <div class="rule" style="left:640px;top:650px;width:250px"></div>
  <div class="rule" style="left:956px;top:650px;width:244px"></div>
  <svg class="front-wheel" width="44" height="44" viewBox="0 0 44 44" aria-hidden="true">
    <g stroke="var(--orange)" fill="none" stroke-width="3" stroke-linecap="round">
      <circle cx="22" cy="22" r="13"/><circle cx="22" cy="22" r="3.5"/>
      <path d="M22 2v40M2 22h40M7.9 7.9l28.2 28.2M36.1 7.9 7.9 36.1"/>
    </g>
  </svg>

  <p class="front-author">BY CAPTAIN DALEN R. HOLTWICK</p>
  <p class="front-creds">USCG-LICENSED CAPTAIN &nbsp;• CERTIFIED BOATING INSTRUCTOR • VETERAN</p>
</main>
</body>
</html>
```